Brochure/flyer for our trip to Paris

Our company is taking us all on a summer trip to Paris. We have some key information that we need to tell everybody about the trip. We think a nicely designed brochure or flyer, which uses our brand colours and guidelines, would be something nice to keep during the trip and as a memento afterwards.

We are looking for a brochure or a flyer which contains all the info in the attached document.

This needs to happen really fast as we actually go to Paris on the 13th August. We also need time to print it!

We can provide a library of icons. All images in the document can be changed. you don't have to use the images in the document.

Target Market(s)

People in our company. They are fun and as this is for a party the flyer needs to feel uplifting.

Industry/Entity Type

Health

Font styles to use
Other font styles liked:
• Nexa - please see attached font.

Requirements
Must have
• Designers must stick to our brand guideline, font and the colours we use.
• Please also see attached content for the flyer.
• This website shows our style - https://www.kelotrix.com/fr
Should not have
• Please don't make it too tacky or too much about French things. It can be a bit playful but not too much.

```html
<!DOCTYPE html>
<html lang="en">
<head>
<meta charset="utf-8">
<title>Kelotrix – Info Guide Paris 2016</title>
<link href="https://fonts.googleapis.com/css2?family=Montserrat:wght@300;400;600;700&family=Questrial&display=swap" rel="stylesheet">
<style>
  :root {
    --brand-blue: #00aeef;
    --brand-white: #ffffff;
    --ink: #1d1d1b;
    --page-bg: #ececec;
    --map-tone: #c3cc5e;
    --map-light: #dfe49c;
    --street-tone: #efe3c4;
    --photo-sky: #dfe3e6;
    --photo-mid: #b9c0c6;
  }
  * { box-sizing: border-box; margin: 0; padding: 0; }
  html, body { width: 1200px; height: 1000px; overflow: hidden; }
  body { background: var(--page-bg); font-family: "Questrial", sans-serif; color: var(--ink); position: relative; }

  .brochure { position: absolute; left: 179px; top: 169px; width: 845px; height: 655px; display: flex; background: var(--brand-white); box-shadow: 0 6px 24px rgba(0,0,0,.18); }
  .panel { height: 100%; position: relative; }

  /* Left panel */
  .panel--info { width: 279px; background: var(--brand-blue); color: var(--brand-white); }
  .travel-section { position: absolute; left: 22px; top: 22px; width: 220px; }
  .hotel-section { position: absolute; left: 22px; top: 292px; width: 220px; }
  .section-title { font-family: "Montserrat", sans-serif; line-height: 1.2; margin-bottom: 6px; }
  .section-title strong { display: block; font-weight: 700; font-size: 24px; letter-spacing: .4px; }
  .section-title span { display: block; font-weight: 300; font-size: 24.5px; letter-spacing: .2px; }
  .journey-label { font-family: "Montserrat", sans-serif; font-weight: 700; font-size: 11px; margin-top: 4px; }
  .journey-text { font-size: 11.5px; line-height: 14.2px; letter-spacing: .5px; padding-left: 10px; text-align: justify; margin-bottom: 6px; }
  .hotel-name { font-family: "Montserrat", sans-serif; font-weight: 700; font-size: 11px; margin-top: 8px; }
  .hotel-details { font-size: 11.5px; line-height: 14.2px; letter-spacing: .5px; }
  .street-map { position: absolute; left: 22px; top: 458px; width: 236px; height: 172px; border: 2px solid rgba(255,255,255,.6); background: linear-gradient(135deg, var(--street-tone), #f6efdc 60%, #e6dab8); }

  /* Middle panel */
  .panel--visits { width: 280px; padding: 14px 8px 0 10px; }
  .visits-heading { font-family: "Montserrat", sans-serif; font-weight: 700; font-size: 13px; color: var(--brand-blue); letter-spacing: .3px; }
  .visits-intro { font-size: 12.6px; line-height: 15px; letter-spacing: .2px; text-align: justify; margin-top: 8px; }
  .visits-note { font-size: 11px; color: var(--brand-blue); margin-top: 8px; }
  .city-map { margin: 12px 0 0 2px; width: 244px; height: 214px; background: linear-gradient(160deg, var(--map-light), var(--map-tone)); }
  .more-heading { margin-top: 24px; }
  .place { margin-top: 5px; }
  .place-name { font-size: 13px; line-height: 16px; color: var(--brand-blue); }
  .place-text { font-size: 13px; line-height: 16px; text-align: justify; }
  .place-link { font-size: 8.6px; line-height: 11px; word-break: break-all; }

  /* Right panel */
  .panel--cover { width: 286px; }
  .cover-brand { position: absolute; left: 55px; top: 55px; }
  .brand-name { font-family: "Montserrat", sans-serif; font-weight: 400; font-size: 50px; color: var(--brand-blue); line-height: 1; }
  .brand-sub { font-family: "Questrial", sans-serif; font-size: 15px; color: var(--brand-blue); margin-top: 10px; letter-spacing: .3px; }
  .cover-photo { position: absolute; left: 0; top: 181px; width: 286px; height: 474px; background: linear-gradient(180deg, #fbfbfb 0%, var(--photo-sky) 35%, var(--photo-mid) 75%, #9ea6ac 100%); }
</style>
</head>
<body>
  <main class="brochure">
    <section class="panel panel--info">
      <div class="travel-section">
        <h2 class="section-title"><strong>TRAVEL</strong><span>INFORMATION</span></h2>
        <p class="journey-label">Outward Journey 13/08/16:</p>
        <p class="journey-text">Meet at Kings Cross St Pancras International Station no later than 6:55am.<br>Our train departs at 7:55am and arrives in paris at 11:17am local time.</p>
        <p class="journey-label">Return Journey 14/08/16:</p>
        <p class="journey-text">Meet at Gare Du Nord no later than 2pm .<br>Our train departs at 3:13pm and arrives in London at 4:30pm local time.</p>
      </div>

      <div class="hotel-section">
        <h2 class="section-title"><strong>HOTEL</strong><span>INFORMATION</span></h2>
        <p class="hotel-name">HOTEL DES TILLEULS</p>
        <p class="hotel-details">12, rue des Lilas<br>75001 Paris France<br>Tel: +33 1 40 00 18 52<br>Nearest Metro Station: Chatelet<br>(as pictured)</p>
      </div>
      <div class="street-map" role="img" aria-label="Street map of the area around the hotel with a location pin"></div>
    </section>

    <section class="panel panel--visits">
      <h3 class="visits-heading">BOOK YOUR VISITS IN PARIS :</h3>
      <p class="visits-intro">If you'd like to see some of the most famous monuments in Paris, we recommend you book your tickets in advance.</p>
      <p class="visits-note">Here are the most touristic places in Paris :</p>
      <div class="city-map" role="img" aria-label="Illustrated map of Paris districts showing the main tourist landmarks"></div>

      <h3 class="visits-heading more-heading">MORE INFORMATION :</h3>
      <div class="place">
        <p class="place-name">Book tickets online for “La Tour eiffel”</p>
        <p class="place-text">(Tube 9 and 6, “Trocadero” station)</p>
        <p class="place-link">http://www.towervisits-paris.example/en/planyourvisit/buyingtickets.html</p>
      </div>
      <div class="place">
        <p class="place-name">Sacré coeur :</p>
        <p class="place-text">Free entrance (Tube 2 and 12)</p>
        <p class="place-link">http://www.hilltopbasilica-paris.example/english/visitandaudioguide/article/openinghours</p>
      </div>
      <div class="place">
        <p class="place-name">Le Louvre :</p>
        <p class="place-text">We advise you to visit the place from outside only, time is too short for the museum</p>
        <p class="place-link">http://www.grandmuseum-paris.example/en/visitortips</p>
      </div>
      <div class="place">
        <p class="place-name">Notre Dame :</p>
        <p class="place-text">Walking distance from the hotel or line 4 (“Cité” station)</p>
        <p class="place-link">http://www.cathedral-paris.example/info.php?article314</p>
      </div>
    </section>

    <section class="panel panel--cover">
      <div class="cover-brand">
        <p class="brand-name">Kelotrix</p>
        <p class="brand-sub">Info Guide Paris 2016</p>
      </div>
      <div class="cover-photo" role="img" aria-label="Photo of a girl holding red balloons in front of the Eiffel Tower on a misty day"></div>
    </section>
  </main>
</body>
</html>
```